Glass repair Packaging Design Project

The product is a glass scratch repair kit inside a clear, plastic clamshell pack.
Two covers need to be designed: one for the front and one for the back of the clamshell pack, both 150mm(height) x 145mm(width).

The scratch repair kit comes in 2 sizes: 2" repair pads and 3" repair pads. Each size kit comes in 3 grades: light scratch removal, medium scratch removal and deep scratch removal.

The main packaging will stay the same for every kit but needs an area on the front cover to say size and grade e.g

2" repair pad, light scratch repair
or
3" repair pad, deep scratch repair

The kit is for the DIY market and so "DIY" needs to be on the front cover quite prominently.
"Drill required but not included" to be on back cover.

Repairable damage includes:
Scuffs
Scratches
Water marks
Acid marks
Wiper blade marks

(front cover)
Glass types suitable for repair include:
patio doors
window units
glass shower screens
glass tables
glass fish tanks
automotive glass
marine glass
domestic glass

The back cover of the pack needs to say the kit contents

This kit contains:
instructions
micro fibre cloth
dust mask
abrasive discs
50ml polishing compound
polishing pads
spray bottle
backing pad for drill

On the bottom of the back cover
www.panevellastore.co.uk

Industry/Entity Type

Automotive

Requirements
Must have
• The colour scheme must work with the logo colours. The logo is black and green.

```html
<!DOCTYPE html>
<html lang="en">
<head>
<meta charset="utf-8">
<title>Panevella DIY Scratch Repair Kit – Pack Covers</title>
<link rel="stylesheet" href="https://fonts.googleapis.com/css2?family=Noto+Sans:wght@700;800&family=Arvo:wght@700&display=swap">
<style>
  :root {
    --sky: #c2def3;
    --leaf: #6bae34;
    --leaf-soft: #8fc164;
    --ink: #111111;
    --white: #ffffff;
    --page: #ffffff;
  }
  * { box-sizing: border-box; margin: 0; padding: 0; }
  html, body { width: 1200px; height: 650px; overflow: hidden; background: var(--page); }
  body { position: relative; font-family: "Noto Sans", Verdana, sans-serif; color: var(--ink); }

  .cover { position: absolute; top: 101px; width: 410px; height: 425px; overflow: hidden; }
  .cover--front { left: 108px; background: var(--sky); }
  .cover--back { left: 650px; background: var(--page); }
  .back-field { position: absolute; left: 0; top: 0; width: 410px; height: 383px; background: var(--sky); }

  .diy-corner { position: absolute; left: 0; top: 0; width: 160px; height: 160px; }
  .diy-label {
    position: absolute; left: 2px; top: 40px; width: 110px; text-align: center;
    transform: rotate(-45deg); font-weight: 800; font-size: 46px; color: var(--leaf);
    -webkit-text-stroke: 2px var(--white); paint-order: stroke fill; letter-spacing: 1px;
  }

  .brand { position: absolute; display: flex; align-items: center; }
  .brand__dot { border-radius: 50%; background: var(--leaf); flex: none; }
  .brand__name { font-weight: 700; color: var(--ink); letter-spacing: -0.5px; }
  .brand--front { left: 118px; top: 52px; gap: 14px; }
  .brand--front .brand__dot { width: 34px; height: 34px; }
  .brand--front .brand__name { font-size: 46px; line-height: 1; }
  .brand--back { left: 32px; top: 36px; gap: 8px; }
  .brand--back .brand__dot { width: 18px; height: 18px; }
  .brand--back .brand__name { font-size: 25px; line-height: 1; }

  .variant { position: absolute; right: 20px; top: 126px; font-size: 14.5px; font-weight: 700; }

  .ornament { position: absolute; }
  .ornament--vine { left: 32px; top: 183px; width: 355px; height: 42px; border-radius: 21px;
    background: linear-gradient(90deg, rgba(107,174,52,0.25), rgba(107,174,52,0.55), rgba(107,174,52,0.25)); }
  .ornament--sprig { left: 33px; top: 104px; width: 158px; height: 40px; border-radius: 20px;
    background: linear-gradient(90deg, rgba(107,174,52,0.7), rgba(17,17,17,0.35), rgba(107,174,52,0.7)); }
  .ornament--bloom { left: 262px; top: 174px; width: 76px; height: 76px; border-radius: 50%;
    background: radial-gradient(circle, #2b3a1c 0%, var(--leaf) 60%, rgba(107,174,52,0.6) 100%); }

  .drill-note { position: absolute; left: 256px; top: 14px; width: 146px; height: 130px; }
  .drill-note__area { position: absolute; inset: 0; border-radius: 6px;
    background: linear-gradient(160deg, var(--leaf-soft), var(--leaf)); }
  .drill-note__text { position: absolute; left: 3px; top: 42px; width: 140px; transform: rotate(-35deg);
    text-align: center; line-height: 1.05; font-weight: 700; color: var(--ink); }
  .drill-note__main { font-size: 20px; }
  .drill-note__small { font-size: 11px; }
  .drill-note__not { font-size: 16px; }

  .section-title { position: absolute; font-family: "Arvo", Georgia, serif; font-weight: 700; color: var(--leaf); white-space: nowrap; }
  .section-title--front { left: 30px; top: 265px; font-size: 17.5px; }
  .section-title--back { left: 35px; top: 168px; font-size: 21px; }

  .bullets { position: absolute; list-style: none; }
  .bullets li { position: relative; padding-left: 21px; font-size: 14px; font-weight: 700; line-height: 21.3px; white-space: nowrap; }
  .bullets li::before {
    content: ""; position: absolute; left: 0; top: 5px; width: 11px; height: 11px; border-radius: 50%;
    border: 1.5px solid var(--ink); background: radial-gradient(circle at 60% 65%, var(--leaf) 0%, var(--leaf) 45%, var(--white) 75%);
  }
  .bullets--glass-a { left: 32px; top: 303px; }
  .bullets--glass-b { left: 234px; top: 303px; }
  .bullets--kit-a { left: 36px; top: 211px; }
  .bullets--kit-b { left: 172px; top: 275px; }

  .web-band { position: absolute; left: 0; top: 386px; width: 410px; height: 39px; background: var(--ink);
    color: var(--white); display: flex; align-items: center; justify-content: center; font-size: 14px; font-weight: 700; }
</style>
</head>
<body>
  <section class="cover cover--front" aria-label="Front cover">
    <svg class="diy-corner" viewBox="0 0 160 160" aria-hidden="true"><polygon points="0,0 150,0 0,155" fill="#111"/></svg>
    <div class="diy-label">DIY</div>

    <div class="brand brand--front"><span class="brand__dot"></span><span class="brand__name">panevella</span></div>
    <p class="variant">2" repair pad, light scratch repair</p>

    <div class="ornament ornament--vine" role="img" aria-label="Decorative leafy vine"></div>

    <h2 class="section-title section-title--front">Glass types suitable for repair include:</h2>
    <ul class="bullets bullets--glass-a">
      <li>patio doors</li><li>window units</li><li>glass shower screens</li><li>glass tables</li>
    </ul>
    <ul class="bullets bullets--glass-b">
      <li>glass fish tanks</li><li>automotive glass</li><li>marine glass</li><li>domestic glass</li>
    </ul>
  </section>

  <section class="cover cover--back" aria-label="Back cover">
    <div class="back-field"></div>
    <div class="brand brand--back"><span class="brand__dot"></span><span class="brand__name">panevella</span></div>

    <div class="ornament ornament--sprig" role="img" aria-label="Decorative leaf sprig"></div>

    <div class="drill-note">
      <div class="drill-note__area" role="img" aria-label="Green leaf illustration behind drill notice"></div>
      <p class="drill-note__text"><span class="drill-note__main">Drill</span> <span class="drill-note__small">required</span><br><span class="drill-note__small">but</span> <span class="drill-note__not">not</span> <span class="drill-note__small">included</span></p>
    </div>

    <h2 class="section-title section-title--back">This kit contains:</h2>
    <div class="ornament ornament--bloom" role="img" aria-label="Decorative leaf star flower"></div>

    <ul class="bullets bullets--kit-a">
      <li>instructions</li><li>micro fibre cloth</li><li>dust mask</li><li>abrasive discs</li>
    </ul>
    <ul class="bullets bullets--kit-b">
      <li>50ml polishing compound</li><li>polishing pads</li><li>spray bottle</li><li>backing pad for drill</li>
    </ul>

    <footer class="web-band">www.panevellastore.co.uk</footer>
  </section>
</body>
</html>
```